Brightfold Sky Advisors needs a wordpress design

New consulting company based in San Francisco focusing on leading businesses (primarily startups) into the cloud. Services include: cloud architecture, security, automation, back-end design, Infrastructure Optimization, Capacity Planning. Even though we are a new company, I'd like to convey a sense of confidence to the prospective client. Logos are attached

Target Market(s)

Start-ups looking to move their application into the cloud

Industry/Entity Type

Information Technology

```html
<!DOCTYPE html>
<html lang="en">
<head>
<meta charset="utf-8">
<title>Brightfold Sky Advisors</title>
<link href="https://fonts.googleapis.com/css2?family=Open+Sans:wght@400;600;700;800&display=swap" rel="stylesheet">
<style>
:root{
  --blue:#1a73c1;
  --blue-dark:#0f4f93;
  --blue-deep:#0b3a70;
  --sky:#3b8fd6;
  --ink:#333;
  --muted:#666;
  --line:#d8d8d8;
  --gray-bg:#e4e4e4;
  --footer:#2a2a2a;
  --white:#fff;
}
*{box-sizing:border-box;margin:0;padding:0}
html,body{width:753px;height:1200px;overflow:hidden}
body{font-family:'Open Sans',Arial,sans-serif;color:var(--ink);background:var(--white);font-size:8px;line-height:1.45}
.wrap{width:600px;margin:0 auto;position:relative}

/* header */
.site-header{height:75px;background:var(--white)}
.site-header .wrap{height:75px}
.brand{position:absolute;left:0;top:14px;display:flex;align-items:center;gap:7px}
.brand-dot{width:16px;height:16px;border-radius:50%;background:var(--blue)}
.brand-name{font-size:15px;font-weight:700;color:var(--blue);letter-spacing:-.2px}
.contact{position:absolute;right:0;top:6px;text-align:right}
.contact small{display:block;font-size:6.5px;color:var(--muted);letter-spacing:.5px}
.contact strong{font-size:12px;color:var(--blue);font-weight:800}
.main-nav{position:absolute;right:0;top:44px;display:flex;gap:4px}
.main-nav a{display:block;font-size:6.5px;font-weight:600;color:var(--ink);text-decoration:none;padding:5px 11px}
.main-nav a.active{background:#222;color:var(--white)}

/* hero */
.hero{height:263px;background:linear-gradient(100deg,var(--blue-deep) 0%,var(--blue) 55%,var(--sky) 100%);position:relative;overflow:hidden;color:var(--white)}
.hero .wrap{height:263px}
.hero h1{position:absolute;left:0;top:22px;font-size:32px;font-weight:400;letter-spacing:-.5px}
.hero h2{position:absolute;left:0;top:70px;width:330px;font-size:15px;font-weight:700;line-height:1.25}
.hero ul{position:absolute;left:0;top:118px;list-style:none}
.hero li{font-size:7.5px;margin-bottom:7px;padding-left:12px;position:relative}
.hero li::before{content:"";position:absolute;left:0;top:3px;width:5px;height:5px;background:var(--white);border-radius:50%}
.hero .btn-outline{position:absolute;left:0;top:203px;border:1.5px solid var(--white);color:var(--white);font-size:7.5px;padding:6px 14px;text-decoration:none;border-radius:2px}
.hero-photo{position:absolute;left:475px;top:0;width:170px;height:263px;background:linear-gradient(180deg,#c9d3de 0%,#3a4a5e 45%,#1d2633 100%)}

/* intro */
.intro{padding-top:34px}
.intro h2{text-align:center;font-size:21px;color:var(--blue);font-weight:700;margin-bottom:10px}
.intro p{font-size:7.5px;color:var(--muted);margin-bottom:10px}

/* feature boxes */
.features{display:flex;justify-content:space-between;margin-top:40px}
.feature{width:180px;height:180px;border:1px solid var(--line);text-align:center;padding:14px 18px;position:relative;box-shadow:0 2px 3px rgba(0,0,0,.08)}
.feature svg{width:34px;height:34px;display:block;margin:0 auto 6px}
.feature h3{font-size:11px;font-weight:800;color:var(--blue);margin-bottom:4px}
.feature p{font-size:6.5px;color:var(--muted)}
.feature .btn{position:absolute;left:50%;bottom:18px;transform:translateX(-50%);background:var(--blue);color:var(--white);font-size:7px;font-weight:700;padding:5px 15px;text-decoration:none;border-radius:2px}
.feature.highlight{background:var(--blue);border-color:var(--blue)}
.feature.highlight h3,.feature.highlight p{color:var(--white)}
.feature.highlight .btn{background:var(--blue-deep)}

/* services */
.services{position:absolute;left:0;top:795px;width:753px;height:280px;background:var(--gray-bg)}
.services .map{position:absolute;inset:0;background:radial-gradient(ellipse at 50% 50%,#d2d2d2 0%,var(--gray-bg) 70%)}
.services h2{position:relative;text-align:center;font-size:15px;font-weight:700;color:#333;padding-top:22px;margin-bottom:22px}
.service-grid{position:relative;display:grid;grid-template-columns:1fr 1fr;column-gap:40px;row-gap:26px}
.service{display:flex;gap:12px}
.service .ico{flex:none;width:34px;height:34px;border-radius:50%;border:2px solid #444;display:flex;align-items:center;justify-content:center}
.service .ico svg{width:18px;height:18px}
.service h4{font-size:8.5px;font-weight:700;color:#333;margin-bottom:3px}
.service p{font-size:6.5px;color:var(--muted)}

/* footer */
.site-footer{position:absolute;left:0;top:1075px;width:753px;height:100px;background:var(--footer);color:#ccc}
.site-footer .wrap{height:100px}
.footer-links{position:absolute;top:16px;list-style:none}
.footer-links li{font-size:6.5px;margin-bottom:4px}
.footer-links.one{left:0}
.footer-links.two{left:110px}
.footer-brand{position:absolute;right:0;top:36px;display:flex;align-items:center;gap:6px}
.footer-brand .brand-dot{width:13px;height:13px}
.footer-brand .brand-name{font-size:12px;color:var(--white)}
.copyright{position:absolute;left:0;top:1175px;width:753px;height:25px;background:var(--blue);color:var(--white);font-size:6.5px;text-align:center;line-height:25px}
</style>
</head>
<body>

<header class="site-header">
  <div class="wrap">
    <div class="brand"><span class="brand-dot"></span><span class="brand-name">Brightfold Sky Advisors</span></div>
    <div class="contact"><small>CONTACT US TODAY</small><strong>1-888-555-0199</strong></div>
    <nav class="main-nav">
      <a class="active" href="#">HOME</a><a href="#">ABOUT</a><a href="#">SERVICES</a><a href="#">PROJECTS</a><a href="#">CONTACT</a>
    </nav>
  </div>
</header>

<section class="hero">
  <div class="wrap">
    <h1>Progressive business thinking</h1>
    <h2>Lorem ips olor sit amet consectetuer adiscing elit raesent vestibulum</h2>
    <ul>
      <li>Lorem ips olor sit amet consectetuer adiscing</li>
      <li>Praesent vestibulum molestie lacus aenean nonummy</li>
      <li>Hendrerit mauris phasellus porta fusce suscipit</li>
    </ul>
    <a class="btn-outline" href="#">CLICK HERE TO LEARN MORE</a>
    <div class="hero-photo" role="img" aria-label="Photo of a smiling businessman in a dark suit"></div>
  </div>
</section>

<section class="intro">
  <div class="wrap">
    <h2>Good solutions for your business!</h2>
    <p>Lorem Ipsum is simply dummy text of the printing and typesetting industry. Lorem Ipsum has been the industry's standard dummy text ever since the 1500s, when an unknown printer took a galley of type and scrambled it to make a type specimen book. It has survived not only five centuries, but also the leap into electronic typesetting.</p>
    <p>Lorem Ipsum has been the industry's standard dummy text ever since the 1500s, when an unknown printer took a galley of type and scrambled it to make a type specimen book. It has survived not only five centuries.</p>

    <div class="features">
      <div class="feature highlight">
        <svg viewBox="0 0 34 34"><rect x="4" y="20" width="5" height="10" fill="#fff"/><rect x="12" y="15" width="5" height="15" fill="#fff"/><rect x="20" y="10" width="5" height="20" fill="#fff"/><path d="M4 15 L14 8 L20 11 L30 3" stroke="#fff" stroke-width="2" fill="none"/></svg>
        <h3>NEW INFORMATION</h3>
        <p>Explore our newest cloud insights and practical guides, made for teams that want to move fast.</p>
        <a class="btn" href="#">MORE</a>
      </div>
      <div class="feature">
        <svg viewBox="0 0 34 34" fill="#222"><circle cx="17" cy="6" r="4"/><rect x="12" y="11" width="10" height="6" rx="2"/><rect x="16" y="17" width="2" height="4"/><rect x="6" y="20" width="22" height="2"/><circle cx="7" cy="25" r="3"/><circle cx="17" cy="25" r="3"/><circle cx="27" cy="25" r="3"/><rect x="4" y="28" width="6" height="5" rx="2"/><rect x="14" y="28" width="6" height="5" rx="2"/><rect x="24" y="28" width="6" height="5" rx="2"/></svg>
        <h3>WHAT DO WE DO?</h3>
        <p>We are committed to providing a service that is personal and tailored for each and every client.</p>
        <a class="btn" href="#">MORE</a>
      </div>
      <div class="feature">
        <svg viewBox="0 0 34 34" fill="#222"><circle cx="11" cy="8" r="4"/><rect x="6" y="13" width="10" height="18" rx="3"/><circle cx="23" cy="8" r="4"/><rect x="18" y="13" width="10" height="18" rx="3"/></svg>
        <h3>WHY CHOOSE US</h3>
        <p>Our advisors offer you choice, security and professional cloud planning. Read more about our partners here.</p>
        <a class="btn" href="#">MORE</a>
      </div>
    </div>
  </div>
</section>

<section class="services">
  <div class="map" role="img" aria-label="Faint world map background"></div>
  <h2>HELPING WITH ANY OF YOUR BUSINESS NEEDS</h2>
  <div class="wrap service-grid">
    <div class="service">
      <span class="ico"><svg viewBox="0 0 18 18" fill="none" stroke="#444" stroke-width="2"><circle cx="9" cy="9" r="4"/><path d="M9 1v3M9 14v3M1 9h3M14 9h3"/></svg></span>
      <div><h4>LOREM IPSUM IS SIMPLY DUMMY TEXT</h4><p>Provide technical and mechanical expertise to clients on cloud architecture, security and automation for growing teams with known industry practice.</p></div>
    </div>
    <div class="service">
      <span class="ico"><svg viewBox="0 0 18 18" fill="none" stroke="#444" stroke-width="2"><path d="M2 16h14M4 16V9M9 16V5M14 16V2"/></svg></span>
      <div><h4>LOREM IPSUM IS SIMPLY DUMMY TEXT</h4><p>Provide technical and mechanical expertise to clients on cloud architecture, security and automation for growing teams with known industry practice.</p></div>
    </div>
    <div class="service">
      <span class="ico"><svg viewBox="0 0 18 18" fill="none" stroke="#444" stroke-width="2"><path d="M3 9l4 4 8-8"/></svg></span>
      <div><h4>LOREM IPSUM IS SIMPLY DUMMY TEXT</h4><p>Provide technical and mechanical expertise to clients on cloud architecture, security and automation for growing teams with known industry practice.</p></div>
    </div>
    <div class="service">
      <span class="ico"><svg viewBox="0 0 18 18" fill="none" stroke="#444" stroke-width="2"><rect x="3" y="3" width="12" height="12" rx="2"/><path d="M6 9h6M9 6v6"/></svg></span>
      <div><h4>LOREM IPSUM IS SIMPLY DUMMY TEXT</h4><p>Provide technical and mechanical expertise to clients on cloud architecture, security and automation for growing teams with known industry practice.</p></div>
    </div>
  </div>
</section>

<footer class="site-footer">
  <div class="wrap">
    <ul class="footer-links one"><li>HOME</li><li>ABOUT US</li><li>PRODUCTS</li><li>CAREER</li></ul>
    <ul class="footer-links two"><li>CONTACT US</li><li>TERMS AND CONDITIONS</li><li>PRIVACY POLICY</li></ul>
    <div class="footer-brand"><span class="brand-dot"></span><span class="brand-name">Brightfold Sky Advisors</span></div>
  </div>
</footer>
<div class="copyright">Copyright 2014 Brightfold Sky Advisors. All rights reserved</div>

</body>
</html>
```